Solarinho 4

Executive Corporate Housing Presentation (B2B Mobility Asset)
We are creating a Corporate Serviced Residence Pitch Deck for international corporate clients (e.g. Velnoria, global mobility teams, relocation departments).
The document is not a traditional real estate brochure. It is a B2B operational housing presentation designed for procurement, HR and corporate mobility decision-makers.
OBJECTIVE
The goal is to communicate:
Operational clarity
Corporate compliance readiness
Location feasibility
Building structure and usability
Executive-level accommodation standard
Reduced relocation and HR friction
DESIGN STYLE
The visual identity should be:
Clean corporate (Harbrook / Corvane / Velnoria style)
Minimalist, high whitespace
Structured and modular (not emotional storytelling)
Data + diagram driven
Subtle luxury (not hospitality marketing)
🚫AVOID
Real estate marketing style
Nestlyo / hospitality visuals
Overly emotional language or lifestyle imagery
Cluttered property listings
Dense technical architectural drawings
KEY VISUAL ELEMENT
Strong emphasis on:
Simplified building diagrams (hotel-style mapping)
Flow-based visuals (how users move through the building)
Corporate icons (access, parking, units, workspace)
Modular information blocks
DESIGN INTENT
The document should feel like:
“A corporate mobility solution presentation”
not
“a luxury property brochure”
Document will be around 12 pages long, I will provide all text and pictures. Enclosed an idea of the desired style. It has to be possible to make changes in the document (PDF - change renders to pictures & change the company's name if needed)
International corporate clients

```html
<!DOCTYPE html>
<html lang="en">
<head>
<meta charset="utf-8">
<title>Solarinho 4 — Executive Corporate Housing</title>
<link href="https://fonts.googleapis.com/css2?family=Sora:wght@400;500;600&display=swap" rel="stylesheet">
<style>
:root{
  --page:#fdcc78;
  --orange:#f08c0a;
  --ink:#1e1e1e;
  --muted:#555;
  --white:#fff;
  --dark:#2a2a2a;
  --card-warm:#fdf5e4;
  --card-warm-line:#f4e2c2;
  --card-peach:#fdf1e6;
  --card-peach-line:#f5dfcc;
  --brand-mark:#dedede;
}
*{margin:0;padding:0;box-sizing:border-box}
html,body{width:1200px;height:2517px;overflow:hidden;background:var(--page)}
body{font-family:"Sora",Arial,sans-serif;color:var(--ink)}
.stage{position:absolute;left:0;top:0;width:1228px;height:2576px;transform:scale(.97720);transform-origin:0 0}
.slide{position:absolute;left:197px;width:834px;height:469px;background:var(--white);overflow:hidden;box-shadow:0 30px 60px rgba(150,90,0,.18)}
.slide svg.art{position:absolute;left:0;top:0;width:834px;height:469px}
.abs{position:absolute}
.tag{position:absolute;height:17px;border:1px solid var(--orange);border-radius:2px;background:var(--white);font-size:9px;line-height:15px;padding-left:8px;color:var(--ink);letter-spacing:.1px}
.tag.soft{border-color:#e6e6e6}
.brand{position:absolute;right:32px;top:18px;font-size:21px;font-weight:600;color:var(--brand-mark)}
.accent{color:var(--orange)}

/* slide 1 */
.cover .title{left:44px;top:160px;font-size:32px;font-weight:600;line-height:40px}
.cover .lede{left:44px;top:302px;width:290px;font-size:11.5px;line-height:18.5px;color:#333}

/* slide 2 */
.challenge .title{left:96px;top:70px;font-size:23.5px;font-weight:600}
.challenge .para{left:551px;top:146px;width:250px;font-size:13.5px;line-height:19.6px;color:#333}
.issue{position:absolute;top:366px;width:230px}
.issue h4{font-size:12px;font-weight:600;padding-left:22px;position:relative}
.issue h4 svg{position:absolute;left:0;top:1px}
.issue p{font-size:8.5px;line-height:12px;color:#777;padding-left:22px;margin-top:4px}
.divider{position:absolute;top:356px;width:1px;height:64px;background:#e2e2e2}

/* slide 3 */
.solution .title{left:44px;top:66px;font-size:31px;font-weight:600}
.solution .intro{left:44px;top:124px;width:760px;font-size:11px;line-height:17px;color:#444}
.feature{position:absolute;width:369px;background:var(--card-warm);border:1px solid var(--card-warm-line);border-radius:3px;padding:12px}
.feature .icon{width:35px;height:35px;border-radius:50%;background:var(--orange);display:flex;align-items:center;justify-content:center}
.feature h3{font-size:15px;font-weight:600;margin-top:17px;color:#2a2a2a}
.feature p{font-size:11px;line-height:16.5px;color:#555;margin-top:9px}

/* slide 4 */
.units .title{left:51px;top:118px;font-size:28px;font-weight:600;line-height:36px;color:var(--white)}
.unit{position:absolute;left:355px;width:437px;height:94px;background:var(--card-peach);border:1px solid var(--card-peach-line);border-radius:3px;padding:18px 18px 0}
.unit h3{font-size:14.5px;font-weight:600;color:#2a2a2a}
.unit p{font-size:11px;line-height:17px;color:#555;margin-top:6px}
</style>
</head>
<body>
<main class="stage">

  <!-- Cover -->
  <section class="slide cover" style="top:206px">
    <svg class="art" viewBox="0 0 834 469" aria-hidden="false">
      <defs>
        <linearGradient id="sky" x1="0" y1="0" x2="0" y2="1">
          <stop offset="0" stop-color="#5b7fb8"/>
          <stop offset=".7" stop-color="#8fa6c9"/>
          <stop offset="1" stop-color="#a69fb0"/>
        </linearGradient>
      </defs>
      <polygon role="img" aria-label="Photo of a glass office tower at dusk" points="485,0 834,0 834,469 398,469" fill="url(#sky)"/>
      <polygon points="834,88 834,469 752,469" fill="var(--dark)"/>
      <polygon points="420,104 463,104 408,374 364,374" fill="var(--orange)"/>
      <polyline points="432,178 370,178 312,469" fill="none" stroke="#f3d7b0" stroke-width="1"/>
      <line x1="432" y1="178" x2="372" y2="469" stroke="#f3d7b0" stroke-width="1"/>
    </svg>
    <div class="tag" style="left:44px;top:116px;width:182px">CORPORATE MOBILITY ASSET</div>
    <h1 class="abs title">Executive<br><span class="accent">Corporate<br>Housing</span></h1>
    <p class="abs lede">A structured, compliance-ready serviced residence solution designed for global mobility teams, HR departments, and procurement decision-makers at multinational organizations.</p>
  </section>

  <!-- The challenge -->
  <section class="slide challenge" style="top:786px">
    <svg class="art" viewBox="0 0 834 469">
      <polygon points="0,0 93,0 78,78 0,78" fill="var(--orange)"/>
      <polygon role="img" aria-label="Photo of an executive signing documents at an office desk" points="98,110 458,110 410,344 35,344" fill="#c9cdd0"/>
      <polygon points="466,110 544,110 490,322 834,322 834,444 8,444 34,344 408,344" fill="var(--orange)"/>
      <rect x="34" y="344" width="768" height="87" fill="var(--white)"/>
    </svg>
    <div class="tag soft" style="left:58px;top:37px;width:162px">THE CHALLENGE</div>
    <div class="brand">Solarinho 4</div>
    <h2 class="abs title">Relocation Friction Is a Business Cost</h2>
    <p class="abs para">Global mobility programs face consistent operational gaps when sourcing temporary housing for transferees. The absence of a standardized, vetted solution creates downstream costs across HR, finance, and compliance.</p>
    <div class="issue" style="left:44px">
      <h4><svg width="15" height="12" viewBox="0 0 15 12"><path d="M1 6h12M8 1l5 5-5 5" fill="none" stroke="var(--orange)" stroke-width="1.4"/></svg>Compliance risk</h4>
      <p>Unverified leases expose organizations<br>to legal and tax liability</p>
    </div>
    <div class="divider" style="left:276px"></div>
    <div class="issue" style="left:298px">
      <h4><svg width="15" height="12" viewBox="0 0 15 12"><path d="M1 6h12M8 1l5 5-5 5" fill="none" stroke="var(--orange)" stroke-width="1.4"/></svg>HR overhead</h4>
      <p>Manual coordination consumes<br>15–20 hours per assignment</p>
    </div>
    <div class="divider" style="left:522px"></div>
    <div class="issue" style="left:550px">
      <h4><svg width="15" height="12" viewBox="0 0 15 12"><path d="M1 6h12M8 1l5 5-5 5" fill="none" stroke="var(--orange)" stroke-width="1.4"/></svg>Employee disruption</h4>
      <p>Delayed housing directly impacts<br>onboarding and productivity</p>
    </div>
  </section>

  <!-- Our solution -->
  <section class="slide solution" style="top:1365px">
    <svg class="art" viewBox="0 0 834 469"><polygon points="0,0 76,0 63,63 0,63" fill="var(--orange)"/></svg>
    <div class="tag soft" style="left:44px;top:23px;width:162px">OUR SOLUTION</div>
    <div class="brand">Solarinho 4</div>
    <h2 class="abs title">One Structured Housing Protocol</h2>
    <p class="abs intro">A fully managed corporate residence program built for operational clarity — not hospitality marketing. Every element is designed to reduce friction for mobility managers and assignees alike.</p>
    <div class="feature" style="left:44px;top:172px;height:131px">
      <div class="icon"><svg width="16" height="16" viewBox="0 0 16 16" fill="none" stroke="#fff" stroke-width="1.2"><path d="M8 1.5l5 2v4c0 3.5-2.5 5.5-5 7-2.5-1.5-5-3.5-5-7v-4z"/><path d="M5.5 8l2 2 3-3.5"/></svg></div>
      <h3>Compliance-Ready</h3>
      <p>Lease structures aligned with corporate policy and local regulations</p>
    </div>
    <div class="feature" style="left:423px;top:172px;height:131px">
      <div class="icon"><svg width="16" height="16" viewBox="0 0 16 16" fill="none" stroke="#fff" stroke-width="1.2"><rect x="2" y="2.5" width="12" height="11" rx="1"/><path d="M2 6h12M6 6v7.5"/></svg></div>
      <h3>Location-Vetted</h3>
      <p>Proximity to business districts, transit hubs, and international schools</p>
    </div>
    <div class="feature" style="left:44px;top:314px;height:114px">
      <div class="icon"><svg width="16" height="16" viewBox="0 0 16 16" fill="none" stroke="#fff" stroke-width="1.2"><circle cx="5.5" cy="10.5" r="3"/><path d="M7.6 8.4L13.5 2.5M11.5 4.5l1.5 1.5"/></svg></div>
      <h3>Turnkey Access</h3>
      <p>Pre-furnished, pre-inspected units with digital onboarding</p>
    </div>
    <div class="feature" style="left:423px;top:314px;height:114px">
      <div class="icon"><svg width="16" height="16" viewBox="0 0 16 16" fill="none" stroke="#fff" stroke-width="1.2"><path d="M4 1.5h6l3 3v10H4z"/><path d="M6 7h5M6 9.5h5M6 12h3"/></svg></div>
      <h3>Single Invoice</h3>
      <p>Consolidated billing with full audit trail for finance teams</p>
    </div>
  </section>

  <!-- Unit standards -->
  <section class="slide units" style="top:1945px">
    <svg class="art" viewBox="0 0 834 469">
      <polygon role="img" aria-label="Photo of a furnished apartment living room with sofas and city windows" points="0,0 352,0 232,469 0,469" fill="#4a4743"/>
      <polygon points="0,0 93,0 75,78 0,78" fill="var(--orange)"/>
      <polygon points="709,448 788,448 783,469 706,469" fill="var(--orange)"/>
    </svg>
    <div class="tag soft" style="left:58px;top:37px;width:162px">UNIT STANDARDS</div>
    <div class="brand">Solarinho 4</div>
    <h2 class="abs title">Executive<br><span class="accent">Accommodation<br>Standard</span></h2>
    <div class="unit" style="top:95px">
      <h3>Studio &amp; 1BR Units</h3>
      <p>Fully furnished with corporate-grade furniture, high-speed internet, in-unit laundry, and kitchenette. Suitable for short-term single assignees.</p>
    </div>
    <div class="unit" style="top:217px">
      <h3>2BR Family Units</h3>
      <p>Expanded floor plans with dedicated workspace, full kitchen, and storage. Designed for family relocations and longer-term assignments.</p>
    </div>
    <div class="unit" style="top:335px">
      <h3>Executive Penthouse</h3>
      <p>Premium configuration with separate living and sleeping areas, enhanced privacy, and priority building access for C-suite and senior leadership.</p>
    </div>
  </section>

</main>
</body>
</html>
```